Catering Menu Package

I currently have a complete menu package, which we have redesigned as far as content, now I need to it put together in a catalog type format. It is essentially 10-12 pages in length, and will be sent for print production. Upon receiving a final edit
Updates

I have added an example gif to the project.

I did this free hand this basically what I am looking for. please change text and type to whatever you think would look best. This is a total rough design so, feel free to change any and everything. The text for the page is on the word documents. If you need more images let me know I am in the process of getting as many images uploaded for your use.

Reason: I figured we got a late jump with questions, so i am extending a few days .

Target Market(s)

The target market is business who wish to have catered luncheons, breakfasts , meetings

Industry/Entity Type

Catering

Requirements
Must have
• I have attached a copy of the text that what we want in the package, our logo, and i have also attached a catering package of another company to give you an idea what the finished product will be
Should not have
• It should not look identical to the example catering packages, these are for some inspiration we want our own design with the same type of look and feel

```html
<!DOCTYPE html>
<html lang="en">
<head>
<meta charset="utf-8">
<title>Light Breakfast Menu – Chesapeake Table Caterers</title>
<link href="https://fonts.googleapis.com/css2?family=Delius&family=Great+Vibes&display=swap" rel="stylesheet">
<style>
  :root{
    --band:#c4a08a;
    --band-light:#e9dcd3;
    --page-top:#ffffff;
    --page-bottom:#ece9e7;
    --heading-rose:#b5578a;
    --heading-plum:#7b4a8c;
    --body:#6a4a3c;
    --note:#555555;
    --brand:#b58a72;
  }
  html,body{margin:0;padding:0;overflow:hidden;}
  body{width:1200px;height:927px;background:#fff;}
  .menu-page{
    position:relative;width:1200px;height:927px;overflow:hidden;
    background:linear-gradient(135deg,var(--page-top) 0%,var(--page-top) 40%,var(--page-bottom) 100%);
    font-family:"Delius",cursive;color:var(--body);
  }
  .side-band{
    position:absolute;left:0;top:0;width:164px;height:927px;background:var(--band);
  }
  .side-band__title{
    position:absolute;left:82px;top:330px;
    transform:translate(-50%,-50%) rotate(90deg);
    white-space:nowrap;
    font-family:"Great Vibes",cursive;font-size:92px;color:#fff;letter-spacing:1px;
  }
  .menu-item{position:absolute;}
  .menu-item h2{
    margin:0 0 2px;font-family:"Delius",cursive;font-size:19px;font-weight:400;
    color:var(--heading-rose);
  }
  .menu-item--right h2{color:var(--heading-plum);}
  .menu-item p{margin:0;font-size:14.3px;line-height:21px;}
  .menu-item .add-on{margin-top:20px;}
  .add-on .price{margin-left:26px;}
  .quick{left:197px;top:20px;width:420px;}
  .fast{left:197px;top:260px;width:420px;}
  .lean{left:197px;top:381px;width:420px;}
  .new-yorker{left:697px;top:153px;width:455px;}
  .city{left:697px;top:347px;width:455px;}
  .pricing-note{
    position:absolute;left:197px;top:522px;margin:0;
    font-family:Arial,Helvetica,sans-serif;font-style:italic;font-size:14px;line-height:18px;color:var(--note);
  }
  .photo{position:absolute;display:block;}
  .photo--fruit{left:500px;top:100px;width:185px;height:162px;}
  .photo--plate{left:618px;top:591px;width:191px;height:127px;}
  .photo--tea{left:821px;top:561px;width:149px;height:199px;}
  .photo--bagel{left:982px;top:618px;width:194px;height:179px;}
  .brand-band{
    position:absolute;left:345px;top:810px;width:855px;height:92px;
    background:linear-gradient(90deg,rgba(233,220,211,0.2) 0%,var(--band-light) 30%,var(--band-light) 100%);
  }
  .brand-mark{
    position:absolute;left:200px;top:720px;width:120px;height:120px;background:var(--band);
  }
  .brand-name{
    position:absolute;left:370px;top:818px;margin:0;
    font-family:"Delius",cursive;font-weight:400;font-size:58px;line-height:76px;color:var(--brand);
    white-space:nowrap;
  }
</style>
</head>
<body>
<main class="menu-page">
  <aside class="side-band"><div class="side-band__title">Light Breakfast</div></aside>

  <section class="menu-item quick">
    <h2>Quick and Easy</h2>
    <p>French Pastry, a Fresh Baked Gourmet Muffin, &amp; Whole Fresh Fruit (featuring Local Apples &amp; Peaches, California Oranges, or Bananas).</p>
  </section>

  <svg class="photo photo--fruit" role="img" aria-label="Bowl of fresh fruit salad with strawberries and mint" viewBox="0 0 185 162">
    <defs><radialGradient id="fruitTone" cx="50%" cy="50%" r="50%">
      <stop offset="0%" stop-color="#d8a24a"/><stop offset="60%" stop-color="#c9b23a"/><stop offset="100%" stop-color="#ffffff"/>
    </radialGradient></defs>
    <rect width="185" height="162" fill="url(#fruitTone)"/>
  </svg>

  <section class="menu-item fast">
    <h2>Fast Farmhouse</h2>
    <p>Fresh baked Breakfast Bread &amp; Buttery Biscuits, Whipped Butter &amp; House-made Strawberry Jam (featuring Local Apples &amp; Peaches, California Oranges, or Bananas).</p>
  </section>

  <section class="menu-item lean">
    <h2>Light and Lean</h2>
    <p>Individual Yogurt, Fresh Fruit &amp; Berry Cups &amp; House-made Granola.</p>
  </section>

  <section class="menu-item menu-item--right new-yorker">
    <h2>New Yorker</h2>
    <p>Brooklyn Bagel, Whipped Cream Cheese, House-made Strawberry Jam &amp; Local Fruit Jellies, Whipped Butter, &amp; Whole Fresh Fruit (featuring Local Apples &amp; Peaches, California Oranges, or Bananas).</p>
    <p class="add-on">Add Smoked Salmon <span class="price">$6.66</span></p>
  </section>

  <section class="menu-item menu-item--right city">
    <h2>City Farmhouse</h2>
    <p>Fresh Baked Buttery Biscuits, Gourmet Muffins &amp; Breakfast Breads, Brooklyn Bagels, Whole Fresh Fruit (featuring Local Apples &amp; Peaches, California Oranges, or Bananas), Whipped Butter &amp; Cream Cheese, House-made Strawberry Jam &amp; Local Fruit Jellies.</p>
  </section>

  <p class="pricing-note">All Prices are per Person, with a 10 person minimum order per item chosen.<br>Local Products used when available &amp; in season</p>

  <svg class="photo photo--plate" role="img" aria-label="Plate of scrambled eggs, bacon, sausage and potatoes" viewBox="0 0 191 127">
    <defs><linearGradient id="plateTone" x1="0" y1="0" x2="1" y2="1">
      <stop offset="0%" stop-color="#e0a640"/><stop offset="55%" stop-color="#f3d45a"/><stop offset="100%" stop-color="#a0502a"/>
    </linearGradient></defs>
    <rect width="191" height="127" fill="url(#plateTone)"/>
  </svg>

  <svg class="photo photo--tea" role="img" aria-label="Breakfast table with teapot, apples and sliced bread" viewBox="0 0 149 199">
    <defs><linearGradient id="teaTone" x1="0" y1="0" x2="0" y2="1">
      <stop offset="0%" stop-color="#d9b070"/><stop offset="50%" stop-color="#c7702e"/><stop offset="100%" stop-color="#7a6a8e"/>
    </linearGradient></defs>
    <rect width="149" height="199" fill="url(#teaTone)"/>
  </svg>

  <svg class="photo photo--bagel" role="img" aria-label="Toasted sesame bagel with butter on a plate" viewBox="0 0 194 179">
    <defs><radialGradient id="bagelTone" cx="50%" cy="50%" r="60%">
      <stop offset="0%" stop-color="#d8b27a"/><stop offset="55%" stop-color="#a67a4c"/><stop offset="100%" stop-color="#c9ccd3"/>
    </radialGradient></defs>
    <rect width="194" height="179" fill="url(#bagelTone)"/>
  </svg>

  <div class="brand-band"></div>
  <div class="brand-mark"></div>
  <p class="brand-name">Chesapeake Table Caterers</p>
</main>
</body>
</html>
```